Food packaging label design

The product name Crispelle, a thin, crispy, and delicious biscuit/cookie made from simple, all natural ingredients. Its name comes from the fact that it looks and tastes a lot like a biscotti cookie, but thinly sliced and much crispier and more delicious than a biscotti. There are currently two flavors: Pure Nutlets, and Almond Cranberry.

I am looking for a fresh, eye catchy design to go on the label for a rice paper stand up pouch (pouch sample attached). Label size are as follows:

4 oz bag - Width X Height
top: 4.5" x 3.5" bottom: 4.5" x 1.5"

12 oz bag
top: 6.5" x 5.5" bottom: 6.5" x 1.5"

I would like for the top portion of the packaging to include:

Crispelle name
Tag line " a thinner, crispier, and more delicious cousin to the biscotti"
simple and natural ingredients

bottom to include:
net weight
ingredients: wheat flour, eggs, sugar, almonds

Attached is a copy of something I created in powerpoint. you can recreate this using graphic designer software per label specs and improve on it or supprise me with something totally awesome. The key is that it that the colors and design needs to pop or contrast against the white rice paper bag and design needs to be eye catchy, fun and whimsical.

Please refer to link below for best practices for creating artwork for labels to ensure correct format for printing.
http://www.vantorprint.example/label-articles/best-practices-designing-custom-labels/

Good luck!

Target Market(s)

educated, health conscious consumers such as customers who shops at meadow pantry, brewvane, market hollis

Industry/Entity Type

Graphic Designer

Requirements
Should not have
• busy or clutter design

```html
<!DOCTYPE html>
<html lang="en">
<head>
<meta charset="utf-8">
<title>Crispelle – Almond Cranberry label</title>
<link href="https://fonts.googleapis.com/css2?family=Lilita+One&family=Courgette&family=Roboto+Condensed:wght@400;700&display=swap" rel="stylesheet">
<style>
  :root {
    --page-bg: #f1f1f1;
    --orange-deep: #f0630f;
    --orange-mid: #f7931e;
    --orange-light: #fdc431;
    --yellow-glow: #ffe27a;
    --band-blue: #2f3193;
    --strip-red: #e8380d;
    --tagline-brown: #5a1a08;
    --name-yellow: #ffd21f;
    --white: #ffffff;
    --ink: #3a2410;
    --cookie-light: #f4dfae;
    --cookie-mid: #e0bc7c;
  }
  * { box-sizing: border-box; margin: 0; padding: 0; }
  html, body { width: 1200px; height: 1000px; overflow: hidden; }
  body { background: var(--page-bg); position: relative; font-family: "Roboto Condensed", sans-serif; }

  .label {
    position: absolute;
    left: 355px; top: 160px;
    width: 490px; height: 680px;
    box-shadow: 0 6px 24px rgba(0,0,0,.15);
  }
  .label-top {
    position: absolute; left: 0; top: 0; width: 100%; height: 333px;
    background:
      radial-gradient(circle at 70% 22%, var(--yellow-glow) 0%, var(--orange-light) 22%, transparent 55%),
      linear-gradient(180deg, var(--orange-mid) 0%, var(--orange-deep) 100%);
  }
  .product-art {
    position: absolute; left: 276px; top: 60px; width: 173px; height: 95px;
    background: linear-gradient(135deg, var(--cookie-light), var(--cookie-mid));
    border-radius: 6px;
    transform: rotate(-12deg);
  }
  .brand-name {
    position: absolute; left: 24px; top: 70px;
    font-family: "Lilita One", sans-serif;
    font-size: 92px; line-height: 1;
    color: var(--name-yellow);
  }
  .tagline {
    position: absolute; left: 46px; top: 222px;
    font-family: "Lilita One", sans-serif;
    font-size: 17px; line-height: 1.2; letter-spacing: .4px;
    color: var(--tagline-brown); text-transform: uppercase;
  }
  .tagline span { display: block; }
  .tagline span + span { padding-left: 78px; }
  .natural-strip {
    position: absolute; left: 0; top: 308px; width: 100%; height: 25px;
    background: linear-gradient(90deg, transparent, var(--strip-red) 25%, var(--strip-red) 75%, transparent);
    color: var(--white); font-weight: 700; font-size: 16px;
    text-align: center; line-height: 25px;
  }
  .band {
    position: absolute; left: 0; width: 100%;
    background: var(--band-blue); color: var(--white);
    font-family: "Courgette", cursive;
    text-align: center;
  }
  .band-flavor { top: 333px; height: 40px; font-size: 25px; line-height: 40px; }
  .band-weight { top: 540px; height: 50px; font-size: 20px; line-height: 50px; }
  .product-window {
    position: absolute; left: 0; top: 373px; width: 100%; height: 167px;
    background: linear-gradient(120deg, var(--cookie-mid), var(--cookie-light) 45%, var(--cookie-mid));
  }
  .label-bottom {
    position: absolute; left: 0; top: 590px; width: 100%; height: 90px;
    background: linear-gradient(180deg, var(--orange-mid), var(--orange-deep));
    text-align: center; color: var(--ink);
    padding-top: 18px;
  }
  .ingredients-title { font-weight: 700; font-size: 15px; }
  .ingredients-list { font-size: 15px; }
</style>
</head>
<body>
  <main class="label">
    <section class="label-top">
      <div class="product-art" role="img" aria-label="Illustration of two thin almond biscotti slices"></div>
      <h1 class="brand-name">Crispelle</h1>
      <p class="tagline"><span>A thinner, crispier, and more</span><span>delicious cousin to the biscotti</span></p>
      <p class="natural-strip">Simple and natural ingredients</p>
    </section>
    <p class="band band-flavor">Almond Cranberry</p>
    <div class="product-window" role="img" aria-label="Clear window showing thin almond cranberry crisps inside the pouch"></div>
    <p class="band band-weight">Net weight: 6 oz</p>
    <section class="label-bottom">
      <p class="ingredients-title">Ingredients:</p>
      <p class="ingredients-list">Wheat flour, eggs, sugar, almonds</p>
    </section>
  </main>
</body>
</html>
```